Business Card & Letterhead Design

We a financial advice company based in Australia. We provide advice to wealthy farmers.

We are changing our business name FROM Brightmere Financial TO Calderstone Wealth and we need a new letterhead and double sided business card design

Attached is designs from our previous branding (Brightmere Financial) as it includes all the details we require on the new Calderstone Wealth business cards and letterhead.

```html
<!DOCTYPE html>
<html lang="en">
<head>
<meta charset="utf-8">
<title>Calderstone Wealth Letterhead</title>
<link rel="stylesheet" href="https://fonts.googleapis.com/css2?family=Cinzel:wght@500&family=Arimo:wght@400;700&family=Great+Vibes&display=swap">
<style>
  :root {
    --brand-orange: #e2703a;
    --ink: #2a2a2a;
    --paper: #ffffff;
  }
  html, body {
    margin: 0;
    padding: 0;
    overflow: hidden;
    background: var(--paper);
  }
  .letterhead {
    position: relative;
    width: 849px;
    height: 1200px;
    overflow: hidden;
    background: var(--paper);
    font-family: "Arimo", Arial, sans-serif;
    color: var(--ink);
  }
  .brand {
    position: absolute;
    top: 16px;
    right: 16px;
    display: flex;
    align-items: center;
    gap: 18px;
  }
  .brand-text {
    display: flex;
    flex-direction: column;
    align-items: stretch;
  }
  .brand-name {
    font-family: "Cinzel", Georgia, serif;
    font-weight: 500;
    font-size: 30px;
    line-height: 34px;
    letter-spacing: 1px;
    color: var(--brand-orange);
    margin: 0;
    white-space: nowrap;
  }
  .brand-tagline {
    margin: 4px 0 0;
    font-size: 13px;
    line-height: 16px;
    letter-spacing: 6.2px;
    color: var(--ink);
    white-space: nowrap;
  }
  .brand-circle {
    width: 94px;
    height: 94px;
    border: 3px solid var(--ink);
    border-radius: 50%;
    box-sizing: border-box;
    flex: none;
  }
  .entity-details {
    position: absolute;
    left: 50px;
    top: 800px;
    font-size: 10px;
    line-height: 14px;
    margin: 0;
  }
  .office-address {
    position: absolute;
    left: 50px;
    top: 940px;
    font-size: 16px;
    line-height: 22px;
    margin: 0;
    font-style: normal;
  }
  .contact-lines {
    position: absolute;
    left: 50px;
    top: 1040px;
    font-size: 16px;
    line-height: 21px;
    margin: 0;
  }
  .contact-lines .label {
    color: var(--brand-orange);
    font-weight: 700;
    margin-right: 4px;
  }
  .licensee-details {
    position: absolute;
    right: 30px;
    top: 955px;
    text-align: right;
    font-size: 12px;
    line-height: 16px;
    margin: 0;
    font-style: normal;
  }
  .referral-line {
    position: absolute;
    right: 30px;
    top: 1090px;
    font-size: 15px;
    color: var(--brand-orange);
    margin: 0;
  }
  .tagline {
    position: absolute;
    right: 28px;
    top: 1108px;
    font-family: "Great Vibes", cursive;
    font-size: 36px;
    color: var(--brand-orange);
    margin: 0;
  }
</style>
</head>
<body>
<main class="letterhead">
  <header class="brand">
    <div class="brand-text">
      <h1 class="brand-name">CALDERSTONE WEALTH</h1>
      <p class="brand-tagline">STRATEGIC FINANCIAL ADVICE</p>
    </div>
    <div class="brand-circle"></div>
  </header>

  <p class="entity-details">
    Corvane Holdings Pty Ltd<br>
    ATF The Ashbury Family<br>
    Trust T/AS Brightmere Financial<br>
    ABN 52 608 117 903<br>
    Corporate Authorised<br>
    Representative of Meridian<br>
    Financial Planning Limited
  </p>

  <address class="office-address">
    Suite 4A, 18 Harlow St<br>
    Riverside QLD 4170<br>
    PO Box 5231<br>
    Eastvale QLD 4170
  </address>

  <p class="contact-lines">
    <span class="label">p</span>(07) 3900 1428<br>
    <span class="label">f</span>(07) 3900 1429
  </p>

  <address class="licensee-details">
    Meridian Financial Planning Limited<br>
    ABN 41 118 520 377<br>
    Australian Financial Services Licence<br>
    Licence Number 318 042<br>
    Principal Address: 410 Fenwick St<br>
    PO Box 6614 Southbank VIC 3006
  </address>

  <p class="referral-line">A referral built business</p>
  <p class="tagline">&ldquo;Financial peace of mind&rdquo;</p>
</main>
</body>
</html>
```